Web design for new streaming audio service

We need a homepage design for a new streaming audio service. Our company is called Olvantra, and we’re basically Vidorama for Audiobooks, Stand-Up Comedy, Lectures, Language Learning, etc. Essentially like Tunelark for everything audio EXCEPT music.
You don’t have to code the homepage (Design Only), but it should include 3 different designs to work with 1) Web; 2) Phones; 3) Tablets.
Below is a link to a mockup of the web version which gives a good idea of what elements we want. This is just a mockup and we want you to improve it.
Once you download the mockup, please refer to the more detailed instructions below:
The following outlines the design project for the Olvantra homepage. We have provided a rough mockup of the homepage layout that gives you a general idea of what we’re going for. There are a few elements that we are attached to, and many others where you have complete creative freedom to do whatever you think looks good.
The ZIP file includes the following:
* Mockup to see what we have in mind (olvantra-homepage-mockup.jpg)
* Text used (olvantra-homepage-text.txt)
* Raw image of actor (olvantra-actor1.jpg)
* Raw images for samples (olvantra-sample-[name].jpg)
Although we have only provided a mockup layout for the web version, we also need you to provide a mobile phone and a tablet version of the design also. It’s very possible the tablet version may be substantially similar to the web version, but the mobile phone version will likely be much different.
All of the raw files are included in the attached ZIP file. Please use our photographs and text as provided although cropping, sizing, etc. is flexible per the instructions below.
Display Requirements:
* Web Version - Minimum resolution 1024x768 (72 dpi) but should look good on 1920x1080 (72 dpi) - Page should be designed to scale to look acceptable in all resolutions in between.
* Phone Version - Minimum Zentro 4 - 640x960 (326 dpi) but should look good on Korvel Nimbus Q5 - 1920x1080 (441 dpi) - Page should be designed to scale to look acceptable in all resolutions and devices in between.
* Tablet Version - Minimum Pagewick Ember LX 7” - 1280x800 (216 dpi) but should also look good on a Slato Breeze - 2048x1536 (264 dpi) - Page should be designed to scale to look acceptable in all resolutions and devices in between.
Above the Fold - We want to make sure the Olvantra logo, Member Login Link, Large Photo, Headline, Price, Button, and the first row of sample images are all “Above the fold”. As a general guideline, this means 600 pixels high on a 1024x768 72 dpi web screen. This requirement is less important on Phone versions.
Top Logo Bar - We want to retain the blue bar with the Olvantra logo on the page, although we are open to a different size, shape and positioning if it greatly enhances the design. Please use the standard logo color, although you are welcome to use either the horizontal or vertical orientation of the logo based on your design.
Text color, font and size - Feel free to design the text in anyway you choose as long as the text is readable on the target platforms.
Buttons - Feel free to use any size, shape and colors for the buttons as long as they are obvious and clickable relative to the page. The only exception is the Chatterly button should follow the Chatterly color scheme and logo treatment (the mockup doesn’t seem 100% correct.)
Top Photograph - We want to retain the large photograph across the top of the screen although final shape and dimensions are flexible.
Size and shape of content samples (i.e. Audiobooks, Stand-Up Comedy, etc.) - Feel free to design the content samples in anyway you choose.
Three Sales Points (i.e. Listen on your Zentro…, All you can enjoy…, etc.) - The Three Sales Points are envisioned to each have a corresponding illustration which you should provide and have rights for. The placeholder is represented by a square next to the text. The color size and shape of these elements are flexible and can be designed in any way you choose.
Opt-in form - Feel free to design the opt-in form in anyway you choose as long as the text is readable and the interactivity is obvious on the target platforms.
Text links and copyright notice - Feel free to design the bottom of the page text links and copyright notice in anyway you choose.
Additional colors, graphic design elements, etc. - Feel free to use any additional colors, graphic design elements, etc. to support your design.

```html
<!DOCTYPE html>
<html lang="en">
<head>
<meta charset="utf-8">
<title>Olvantra – Unlimited Listening</title>
<link rel="stylesheet" href="https://fonts.googleapis.com/css2?family=Questrial&family=Open+Sans:wght@400;600;700&display=swap">
<style>
  :root {
    --brand-blue: #5aabd6;
    --brand-blue-deep: #1d5f8a;
    --login-bg: #d9ecf6;
    --cta-red: #ee5656;
    --chat-blue: #3b5998;
    --ink: #222;
    --muted: #8a8f94;
    --band: #f4f4f4;
    --dark: #2a2a2a;
    --darker: #1d1d1d;
    --input-bg: #1c1c1c;
    --line: #c9d6de;
  }
  * { box-sizing: border-box; margin: 0; padding: 0; }
  html, body { width: 928px; height: 1200px; overflow: hidden; background: #fff; }
  body { position: relative; font-family: "Open Sans", Arial, sans-serif; color: var(--ink); }

  /* Hero */
  .hero { position: absolute; left: 0; top: 0; width: 928px; height: 410px; background: #fff; }
  .hero-photo {
    position: absolute; left: 0; top: 0; width: 928px; height: 410px;
    background:
      radial-gradient(ellipse 260px 230px at 300px 220px, #d9a583 0%, #c98f6e 40%, rgba(201,143,110,0) 75%),
      linear-gradient(180deg, rgba(255,255,255,0) 70%, rgba(58,74,102,.9) 100%),
      linear-gradient(90deg, #e9dfd6 0%, #d8c0ad 35%, #efe7e1 62%, #ffffff 78%);
  }
  .topbar {
    position: absolute; left: 125px; top: 18px; width: 678px; height: 48px;
    background: var(--brand-blue);
  }
  .brand { position: absolute; left: 8px; top: 8px; display: flex; align-items: center; gap: 6px; }
  .brand-dot { width: 28px; height: 28px; border-radius: 50%; background: #fff; }
  .brand-name { font-family: "Questrial", sans-serif; font-size: 23px; color: #fff; }
  .login-btn {
    position: absolute; right: 12px; top: 10px; width: 78px; height: 27px;
    background: var(--login-bg); border-radius: 3px;
    font-size: 10px; font-weight: 600; color: var(--brand-blue-deep);
    display: flex; align-items: center; justify-content: center;
  }
  .hero-copy { position: absolute; left: 470px; top: 152px; width: 278px; text-align: center; }
  .hero-title { font-family: "Questrial", sans-serif; font-weight: 400; font-size: 28px; line-height: 33px; color: var(--brand-blue-deep); }
  .hero-price { font-family: "Questrial", sans-serif; font-size: 16px; margin-top: 8px; color: #111; }
  .cta {
    display: inline-flex; align-items: center; justify-content: center;
    width: 174px; height: 37px; margin-top: 14px;
    background: var(--cta-red); color: #fff; font-weight: 600; font-size: 14px;
  }
  .hero-note { margin-top: 5px; font-size: 10px; font-weight: 700; color: var(--brand-blue-deep); }

  /* Samples */
  .samples-title {
    position: absolute; top: 451px; left: 0; width: 928px; text-align: center;
    font-family: "Questrial", sans-serif; font-size: 19px; color: #222;
  }
  .divider { position: absolute; left: 392px; width: 144px; height: 10px; }
  .sample-grid { position: absolute; left: 125px; top: 517px; width: 680px; }
  .sample { position: absolute; display: flex; align-items: center; width: 170px; height: 70px; }
  .sample-cover { width: 70px; height: 70px; flex: none; }
  .sample-label { margin-left: 17px; font-size: 9.5px; line-height: 12px; color: #222; }

  /* Selling points */
  .points { position: absolute; left: 0; top: 726px; width: 928px; height: 92px; background: var(--band); }
  .point { position: absolute; top: 16px; display: flex; align-items: center; }
  .point svg { flex: none; }
  .point-text { margin-left: 18px; width: 140px; font-size: 9.5px; line-height: 12px; color: var(--muted); }

  /* Sign-up */
  .signup { position: absolute; left: 0; top: 818px; width: 928px; height: 332px; background: var(--dark); text-align: center; }
  .signup-mark { position: absolute; left: 456px; top: 50px; width: 16px; height: 16px; border-radius: 50%; background: #fff; }
  .signup-title { position: absolute; top: 110px; width: 928px; font-family: "Questrial", sans-serif; font-size: 14px; color: #fff; }
  .signup-copy { position: absolute; top: 161px; left: 244px; width: 440px; font-size: 8px; line-height: 12px; color: #9a9a9a; }
  .signup-note { position: absolute; top: 192px; width: 928px; font-size: 8px; color: #9a9a9a; }
  .email-field {
    position: absolute; left: 340px; top: 224px; width: 249px; height: 26px;
    background: var(--input-bg); border: 1px solid #3a3a3a;
    font-size: 8px; color: #777; display: flex; align-items: center; justify-content: center;
  }
  .btn { position: absolute; top: 270px; height: 27px; display: flex; align-items: center; color: #fff; font-size: 10.5px; font-weight: 700; }
  .btn-access { left: 299px; width: 156px; background: var(--cta-red); }
  .btn-access .btn-icon { width: 30px; height: 27px; display: flex; align-items: center; justify-content: center; border-right: 1px solid rgba(255,255,255,.25); }
  .btn-access span { flex: 1; text-align: center; }
  .or { position: absolute; left: 456px; top: 277px; width: 16px; font-size: 9px; color: #aaa; }
  .btn-chat { left: 472px; width: 157px; background: var(--chat-blue); justify-content: center; gap: 7px; }
  .btn-chat .sq { width: 12px; height: 12px; background: #fff; }

  /* Footer */
  .footer { position: absolute; left: 0; top: 1150px; width: 928px; height: 50px; background: var(--darker); text-align: center; }
  .to-top { position: absolute; left: 456px; top: -8px; width: 16px; height: 16px; border-radius: 50%; background: var(--darker); }
  .footer-links { position: absolute; top: 12px; width: 928px; font-size: 8px; color: #aaa; }
  .footer-links a { color: #aaa; text-decoration: none; margin: 0 5px; }
  .copyright { position: absolute; top: 30px; width: 928px; font-size: 8px; color: #888; }
</style>
</head>
<body>

<header class="hero">
  <div class="hero-photo" role="img" aria-label="Smiling young man wearing headphones, looking at his phone"></div>
  <div class="topbar">
    <div class="brand"><span class="brand-dot"></span><span class="brand-name">Olvantra</span></div>
    <a class="login-btn">Member Login</a>
  </div>
  <div class="hero-copy">
    <h1 class="hero-title">Unlimited Listening.<br>Wherever you are.</h1>
    <p class="hero-price">Only $9.99 per month</p>
    <a class="cta">Start Your Free Trial</a>
    <p class="hero-note">* Credit Card Not Required</p>
  </div>
</header>

<section class="samples">
  <h2 class="samples-title">A sample of what you can listen to on Olvantra</h2>
  <svg class="divider" style="top:483px" viewBox="0 0 144 10">
    <line x1="0" y1="5" x2="144" y2="5" stroke="var(--line)" stroke-width="1"/>
    <circle cx="72" cy="5" r="4" fill="var(--brand-blue)"/>
  </svg>
  <div class="sample-grid">
    <div class="sample" style="left:0;top:0"><div class="sample-cover" role="img" aria-label="Audiobook cover" style="background:linear-gradient(#2f4a55,#10222a)"></div><span class="sample-label">Audiobooks</span></div>
    <div class="sample" style="left:173px;top:0"><div class="sample-cover" role="img" aria-label="Stand-up comedy album cover" style="background:linear-gradient(#a33a2c,#5a4a40)"></div><span class="sample-label">Stand-Up<br>Comedy</span></div>
    <div class="sample" style="left:347px;top:0"><div class="sample-cover" role="img" aria-label="Language course cover" style="background:linear-gradient(#1d8fd8,#0c4a8a)"></div><span class="sample-label">Language<br>Learning</span></div>
    <div class="sample" style="left:521px;top:0"><div class="sample-cover" role="img" aria-label="Memoir cover" style="background:linear-gradient(#cfd8d6,#9fcf7a)"></div><span class="sample-label">Biographies &amp;<br>Memoirs</span></div>
    <div class="sample" style="left:0;top:93px"><div class="sample-cover" role="img" aria-label="Meditation album cover" style="background:linear-gradient(#b06bc0,#6a3a8a)"></div><span class="sample-label">Guided<br>Meditations</span></div>
    <div class="sample" style="left:173px;top:93px"><div class="sample-cover" role="img" aria-label="Business training cover" style="background:linear-gradient(#6a1f1f,#2a1a1a)"></div><span class="sample-label">Business<br>Training</span></div>
    <div class="sample" style="left:347px;top:93px"><div class="sample-cover" role="img" aria-label="Celebrity interview cover" style="background:linear-gradient(#8a6a5a,#3a2a2a)"></div><span class="sample-label">Celebrity<br>Interviews</span></div>
    <div class="sample" style="left:521px;top:93px"><div class="sample-cover" role="img" aria-label="Fitness program cover" style="background:linear-gradient(#4ab0e0,#e04a6a)"></div><span class="sample-label">Fitness<br>Programs</span></div>
  </div>
</section>

<section class="points">
  <div class="point" style="left:125px">
    <svg width="60" height="60" viewBox="0 0 60 60"><polygon points="30,0 39,9 51,9 51,21 60,30 51,39 51,51 39,51 30,60 21,51 9,51 9,39 0,30 9,21 9,9 21,9" fill="var(--brand-blue)"/>
      <rect x="19" y="20" width="10" height="18" rx="1.5" fill="none" stroke="#fff" stroke-width="1.5"/><rect x="31" y="24" width="10" height="16" rx="1.5" fill="none" stroke="#fff" stroke-width="1.5"/></svg>
    <p class="point-text">Listen on your Zentro, Slato or Robexa device.</p>
  </div>
  <div class="point" style="left:357px">
    <svg width="60" height="60" viewBox="0 0 60 60"><polygon points="30,0 39,9 51,9 51,21 60,30 51,39 51,51 39,51 30,60 21,51 9,51 9,39 0,30 9,21 9,9 21,9" fill="var(--brand-blue)"/>
      <path d="M22 24 L30 18 L38 24 L38 42 L22 42 Z" fill="none" stroke="#fff" stroke-width="1.5"/><circle cx="30" cy="25" r="2" fill="#fff"/></svg>
    <p class="point-text">All you can enjoy for one low monthly price.</p>
  </div>
  <div class="point" style="left:589px">
    <svg width="60" height="60" viewBox="0 0 60 60"><polygon points="30,0 39,9 51,9 51,21 60,30 51,39 51,51 39,51 30,60 21,51 9,51 9,39 0,30 9,21 9,9 21,9" fill="var(--brand-blue)"/>
      <path d="M21 18 H33 L38 23 V42 H21 Z" fill="none" stroke="#fff" stroke-width="1.5"/><circle cx="36" cy="38" r="5" fill="#fff"/><path d="M34 36 L38 40 M38 36 L34 40" stroke="var(--brand-blue)" stroke-width="1.3"/></svg>
    <p class="point-text">No obligation. Cancel any time.</p>
  </div>
</section>

<section class="signup">
  <span class="signup-mark"></span>
  <h2 class="signup-title">Start Your Free Trial</h2>
  <svg class="divider" style="top:136px" viewBox="0 0 144 10">
    <line x1="0" y1="5" x2="144" y2="5" stroke="#555" stroke-width="1"/>
    <circle cx="72" cy="5" r="4" fill="#666"/>
  </svg>
  <p class="signup-copy">You will get instant &amp; unlimited access to all the material on Olvantra for 14 days. There is no obligation &amp; you can cancel at any time.</p>
  <p class="signup-note">Credit Card Not Required for Free Trial</p>
  <div class="email-field">Your Email Address</div>
  <a class="btn btn-access"><span class="btn-icon"><svg width="14" height="10" viewBox="0 0 14 10"><rect x="0.5" y="0.5" width="13" height="9" fill="none" stroke="#fff"/><path d="M0.5 0.5 L7 6 L13.5 0.5" fill="none" stroke="#fff"/></svg></span><span>Get Instant Access</span></a>
  <span class="or">or</span>
  <a class="btn btn-chat"><span class="sq"></span>Sign Up Using Chatterly</a>
</section>

<footer class="footer">
  <span class="to-top"><svg width="16" height="16" viewBox="0 0 16 16"><path d="M5 9 L8 6 L11 9" fill="none" stroke="#888" stroke-width="1.3"/></svg></span>
  <nav class="footer-links"><a>About</a><a>Help</a><a>Contact Us</a><a>Member Login</a><a>Privacy Policy</a><a>Terms of Service</a></nav>
  <p class="copyright">©2014 Olvantra LLC - All Rights Reserved</p>
</footer>

</body>
</html>
```